Jazz: Journey Through the Harlem Renaissance and the Black Arts Movement

Corvel Lounge invites you on a musical Journey Through the Harlem Renaissance and the Black Arts Movement!
Join us for an afternoon of Jazz on Sunday, February 27, 2022 from 3pm – 5pm.
Local jazz artists will thrill you with the music of legendary Harlem Renaissance artists such as Earl Whitcombe and Rosie Tamberly and famed Black Arts Movement stylings reminiscent of Amos Verrick and Leda Farrow.
There will be games, prizes and opportunities to support arts programs at local schools.

```html
<!DOCTYPE html>
<html lang="en">
<head>
<meta charset="utf-8">
<title>Jazz: Journey Through the Harlem Renaissance and the Black Arts Movement</title>
<link rel="stylesheet" href="https://fonts.googleapis.com/css2?family=Libre+Caslon+Text:wght@400;700&family=Montserrat:ital,wght@0,400;0,500;0,600;0,700;0,800;1,600&family=Russo+One&display=swap">
<style>
  :root {
    --ink: #1e2d33;
    --ink-soft: #2b3c43;
    --gold: #e9b92f;
    --gold-deep: #c99a1e;
    --white: #ffffff;
    --line: #d8d8d8;
    --page: #ffffff;
  }
  * { margin: 0; padding: 0; box-sizing: border-box; }
  html, body { width: 727px; height: 1200px; overflow: hidden; background: var(--page); }
  .canvas { position: relative; width: 727px; height: 1200px; }

  .flyer {
    position: absolute; left: 0; top: 108px;
    width: 727px; height: 983px;
    background: var(--ink);
    overflow: hidden;
    font-family: "Montserrat", sans-serif;
    color: var(--white);
  }
  .abs { position: absolute; }
  .center-text { left: 0; width: 100%; text-align: center; }

  .staff-ornament {
    position: absolute; top: 72px; height: 278px;
    background: radial-gradient(ellipse at 50% 60%, rgba(233,185,47,0.22), rgba(233,185,47,0) 70%);
  }
  .staff-ornament--left { left: 17px; width: 256px; }
  .staff-ornament--right { left: 448px; width: 256px; }

  .venue-mark {
    top: 70px; left: 0; width: 100%;
    display: flex; flex-direction: column; align-items: center; gap: 6px;
  }
  .venue-mark__circle {
    width: 46px; height: 46px; border-radius: 50%;
    border: 2px solid var(--gold);
  }
  .venue-mark__name {
    font-family: "Montserrat", sans-serif; font-weight: 600;
    font-size: 15px; letter-spacing: 4px; color: var(--gold);
    text-transform: uppercase;
  }

  .host-name {
    top: 203px; font-family: "Libre Caslon Text", serif; font-weight: 700;
    font-size: 40px; color: var(--gold); line-height: 50px;
  }
  .invite-line {
    top: 256px; font-family: "Libre Caslon Text", serif; font-weight: 400;
    font-size: 30px; line-height: 40px;
  }

  .era-box {
    left: 94px; top: 317px; width: 536px; height: 64px;
    background: var(--ink);
    border: 1.5px solid var(--gold); border-top: none;
    box-shadow: 0 5px 6px rgba(0,0,0,0.35);
    z-index: 2;
  }
  .era-box__rule {
    position: absolute; top: 0; height: 1.5px; background: var(--gold);
  }
  .era-box__rule--left { left: 0; width: 174px; }
  .era-box__rule--right { right: 0; width: 162px; }
  .era-box__kicker {
    position: absolute; top: -12px; left: 0; width: 100%; text-align: center;
    font-weight: 600; font-size: 18px; color: var(--gold); letter-spacing: 1px; line-height: 24px;
  }
  .era-box__title {
    position: absolute; top: 14px; left: 0; width: 100%; text-align: center;
    font-weight: 500; font-size: 37px; line-height: 46px; letter-spacing: 0.5px;
  }

  .headline-band {
    left: 0; top: 351px; width: 727px; height: 286px;
    background: var(--gold);
  }
  .headline { display: block; }

  .details {
    left: 0; top: 637px; width: 727px; height: 346px;
    background: linear-gradient(115deg, var(--ink-soft) 0%, var(--ink) 45%, #34464d 75%, var(--ink) 100%);
  }

  .join { left: 94px; top: 655px; font-weight: 800; font-size: 54px; line-height: 58px; letter-spacing: 1px; }
  .afternoon {
    left: 94px; top: 715px; font-weight: 600; font-size: 26px; line-height: 32px; color: var(--gold);
  }
  .divider { left: 374px; top: 663px; width: 2px; height: 132px; background: var(--white); }

  .month { left: 416px; top: 658px; font-weight: 700; font-size: 35px; line-height: 40px; color: var(--gold); letter-spacing: 1px; }
  .day { left: 414px; top: 690px; font-weight: 800; font-size: 100px; line-height: 110px; letter-spacing: -2px; }
  .day-suffix { left: 538px; top: 700px; font-weight: 800; font-size: 56px; line-height: 60px; }
  .year { left: 538px; top: 748px; font-weight: 700; font-size: 31px; line-height: 36px; color: var(--gold); }

  .program {
    left: 58px; top: 816px; width: 612px; height: 93px;
    border: 1.5px solid var(--line); border-radius: 12px;
  }
  .program__text {
    position: absolute; left: 14px; right: 14px; top: 33px;
    text-align: center; font-size: 12px; line-height: 14.5px; font-weight: 500;
  }
  .time-pill {
    left: 250px; top: 798px; width: 240px; height: 38px;
    background: var(--gold); color: var(--ink); border-radius: 12px;
    text-align: center; font-weight: 700; font-size: 23px; line-height: 38px; letter-spacing: 1px;
    z-index: 2;
  }
  .extras {
    top: 920px; font-style: italic; font-weight: 600; font-size: 14.5px; line-height: 18px; color: var(--gold);
  }
</style>
</head>
<body>
<div class="canvas">
  <article class="flyer">
    <div class="staff-ornament staff-ornament--left" role="img" aria-label="Curved gold music staff with treble clef and notes"></div>
    <div class="staff-ornament staff-ornament--right" role="img" aria-label="Curved gold music staff with treble clef and notes"></div>

    <div class="abs venue-mark">
      <span class="venue-mark__circle"></span>
      <span class="venue-mark__name">Corvel Lounge</span>
    </div>

    <h1 class="abs center-text host-name">Corvel Lounge</h1>
    <p class="abs center-text invite-line">Invites you on a musical Journey</p>

    <div class="abs headline-band">
      <svg class="headline" width="727" height="286" viewBox="0 0 727 286" aria-label="The Black Arts Movement!">
        <line x1="229" y1="73" x2="301" y2="73" stroke="#1e2d33" stroke-width="2"/>
        <line x1="432" y1="73" x2="505" y2="73" stroke="#1e2d33" stroke-width="2"/>
        <text x="366" y="90" text-anchor="middle" font-family="Russo One, sans-serif" font-size="46" fill="#1e2d33">THE</text>
        <text x="66" y="178" textLength="595" lengthAdjust="spacingAndGlyphs" font-family="Russo One, sans-serif" font-size="96" fill="#1e2d33">BLACK ARTS</text>
        <text x="66" y="262" textLength="595" lengthAdjust="spacingAndGlyphs" font-family="Russo One, sans-serif" font-size="96" fill="#1e2d33">MOVEMENT!</text>
      </svg>
    </div>

    <div class="abs era-box">
      <span class="era-box__rule era-box__rule--left"></span>
      <span class="era-box__rule era-box__rule--right"></span>
      <span class="era-box__kicker">THROUGH THE</span>
      <span class="era-box__title">Harlem Renaissance</span>
    </div>

    <section class="abs details" role="img" aria-label="Dim photo of a jazz musician performing on stage"></section>

    <h2 class="abs join">JOIN US</h2>
    <p class="abs afternoon">For an afternoon<br>of Jazz on Sunday</p>
    <span class="abs divider"></span>

    <p class="abs month">FEBRUARY</p>
    <p class="abs day">27</p>
    <p class="abs day-suffix">TH</p>
    <p class="abs year">2022</p>

    <div class="abs time-pill">FROM 3PM – 5PM</div>
    <div class="abs program">
      <p class="program__text">Local jazz artists will thrill you with the music of legendary Harlem Renaissance artists such as Earl Whitcombe and Rosie Tamberly and famed Black Arts Movement stylings reminiscent of Amos Verrick and Leda Farrow.</p>
    </div>

    <p class="abs center-text extras">There will be games, prizes and opportunities to support<br>arts programs at local schools</p>
  </article>
</div>
</body>
</html>
```